NFVPS Business Card Revamp: Professional and Modern Design for Enhanced Networking

The Northfield Veterinary Practitioner Society (NFVPS) is seeking a redesign of its current business cards to better represent its professional image and improve its networking capabilities. The NFVPS is a professional association for veterinary technologists in Alberta, Canada, and it aims to promote the welfare of animals and the veterinary profession through continuing education, advocacy, and professional development.

The project objectives are to create a professional and modern design for the NFVPS business cards that accurately reflects the organization's values and mission. We would like to include our brand colors in the final design and make it editable to update different roles and positions for the association. The card will need to include the name, pronouns (if applicable), and position of the individual as well as an email address, phone, and website.

The final deliverables for this project will include a design concept for the new NFVPS business cards, a layout for the business cards that includes all relevant contact information and branding elements, and final design files in an editable format.

Target Market(s)

Members, industry stakeholders, government

Industry/Entity Type

Veterinary

Contact Information for Business Card

Name, pronouns (if applicable), title, logo, website, email, phone number

Font styles to use
Other font styles liked:
• Open Sans, logo font is Politica

Requirements
Must have
• Brand recognition, logo, professional and modern design
Nice to have
• double-sided - open to single sided
Should not have
• pictures of animals, hearts

```html
<!DOCTYPE html>
<html lang="en">
<head>
<meta charset="utf-8">
<title>NFVPS Business Card</title>
<link href="https://fonts.googleapis.com/css2?family=Roboto+Condensed:wght@400;700&display=swap" rel="stylesheet">
<style>
  :root {
    --backdrop: #e4e4e2;
    --paper: #f7f7f6;
    --slate: #586e6e;
    --sky: #5aacc6;
    --leaf: #7aab45;
    --white: #ffffff;
  }
  html, body {
    margin: 0;
    width: 1200px;
    height: 1200px;
    overflow: hidden;
    background: var(--backdrop);
    font-family: "Roboto Condensed", sans-serif;
  }
  .canvas { position: relative; width: 1200px; height: 1200px; }
  .card {
    position: absolute;
    left: 262px;
    width: 686px;
    height: 392px;
    border-radius: 26px;
    overflow: hidden;
    box-shadow: 0 14px 22px rgba(0,0,0,0.28);
  }
  .card-front { top: 165px; background: var(--paper); }
  .card-back { top: 653px; background: var(--slate); }

  .brand {
    position: absolute;
    text-align: center;
    font-weight: 400;
    line-height: 1;
  }
  .brand-mark {
    display: block;
    font-size: 66px;
    letter-spacing: 1px;
  }
  .brand-name {
    display: block;
    font-size: 11px;
    margin-top: 4px;
    letter-spacing: 0.1px;
  }
  .card-front .brand { left: 100px; width: 214px; top: 116px; color: var(--slate); }
  .card-back .brand { left: 193px; width: 300px; top: 140px; color: var(--white); }
  .card-back .brand-mark { font-size: 82px; }
  .card-back .brand-name { font-size: 13.5px; margin-top: 6px; }
  .brand-dot {
    display: block;
    margin: 0 auto 14px;
    width: 40px; height: 40px;
    border-radius: 50%;
    background: var(--leaf);
  }
  .card-front .brand-dot { width: 30px; height: 30px; margin-bottom: 10px; }

  .divider {
    position: absolute;
    left: 327px; top: 76px;
    width: 1.5px; height: 184px;
    background: linear-gradient(var(--slate), rgba(88,110,110,0.15));
  }
  .person { position: absolute; left: 356px; top: 96px; color: var(--slate); }
  .person-name { margin: 0; font-size: 27px; font-weight: 700; letter-spacing: 0.3px; line-height: 1; }
  .person-role { margin: 6px 0 0; font-size: 18px; font-weight: 400; line-height: 1; }

  .contacts { position: absolute; left: 356px; top: 176px; margin: 0; padding: 0; list-style: none; }
  .contacts li {
    display: flex; align-items: center;
    height: 23.5px;
    font-size: 20px;
    color: #3f4c4c;
  }
  .contacts svg { width: 14px; height: 14px; margin-right: 10px; fill: var(--sky); flex: none; }

  .tagline-band {
    position: absolute;
    left: 0; top: 336px;
    width: 100%; height: 26px;
    background: var(--sky);
    color: var(--white);
    text-align: center;
    font-size: 19px;
    line-height: 26px;
    letter-spacing: 1.6px;
  }
</style>
</head>
<body>
<main class="canvas">
  <section class="card card-front">
    <div class="brand">
      <span class="brand-dot"></span>
      <span class="brand-mark">NFVPS</span>
      <span class="brand-name">Northfield Veterinary Practitioner Society</span>
    </div>
    <div class="divider"></div>
    <div class="person">
      <h1 class="person-name">DANA WHITFIELD,RVT</h1>
      <p class="person-role">President</p>
    </div>
    <ul class="contacts">
      <li>
        <svg viewBox="0 0 16 16"><path d="M3.6 1.2l2.3 2.6-1.2 1.9c.9 2 2.6 3.8 4.7 4.8l1.9-1.2 2.6 2.3-1.4 2.3C7.4 13.9 2.1 8.6 1.3 2.6z"/></svg>
        555.014.2290
      </li>
      <li>
        <svg viewBox="0 0 16 16"><path d="M1 3.5h14v9H1z M1.8 4.2L8 8.8l6.2-4.6" fill="none" stroke="#5aacc6" stroke-width="1.4"/></svg>
        info@nfvps.org
      </li>
      <li>
        <svg viewBox="0 0 16 16"><circle cx="8" cy="8" r="7"/><path d="M4 5.5c1.2-.8 2.2.4 3 1.2.6.7-.4 1.6-1.2 2 .4 1.2 1.3 2 1 3.3M10.5 3.2c-.6 1 .4 1.8 1.4 1.6.8.9.7 2.2.2 3.2" fill="none" stroke="#f7f7f6" stroke-width="1.1"/></svg>
        www.nfvps.org
      </li>
    </ul>
    <div class="tagline-band">support.advance.unite</div>
  </section>

  <section class="card card-back">
    <div class="brand">
      <span class="brand-dot"></span>
      <span class="brand-mark">NFVPS</span>
      <span class="brand-name">Northfield Veterinary Practitioner Society</span>
    </div>
  </section>
</main>
</body>
</html>
```